Kavenzira Wines

A Red Wine Label for future Wine Concept called Kavenzira Wine. The back label will have the following words which capture the essence of the wine "I am sworn to the secrecy about the origins of this wine but I can assure you it’s from the best cellars of Africa. Kavenzira is an African (Shona) name which loosely means honour, praise or to be held in high exteem. Hold on to your hats because this wine is a whirlwind of flavours. It's dark, spicy and fruity flavours will attack the palate with warm aggression and intent whilst being served with Sadza/ Nsima and roasted beef accompanied with mufushwa (dried vegetables) cooked in grounded nut paste. The inspiring flame, style and mood of an African braai, together with its outlandish flavours popping in and out of the glass, Kavenzira will make every serving a gesture of respect and distinction!!!"
Updates

I will be buying wine packed in unbranded bottles then Brand it as Kavenzira on my own Kavenzira label for some African event theme. The wines will be South African a Shiraz. So I need a back label with message placed in brief and front label for a red wine bottle. I have attached some old labels for the wine so I need a redesign of the l label for have a morden and African feel to it                                   

Please

Target Market(s)

Appeal to general populace and those with an afrocentric feel

Requirements
Must have
• Back and front labels, simplicity
Should not have
• Too many colours

```html
<!DOCTYPE html>
<html lang="en">
<head>
<meta charset="utf-8">
<title>Kavenzira Wine – Shiraz Labels</title>
<link rel="stylesheet" href="https://fonts.googleapis.com/css2?family=Open+Sans:wght@400;600&display=swap">
<style>
  :root {
    --backdrop: #d9d9d9;
    --label-bg: #ecf2b8;
    --label-edge: #d6dea0;
    --ink: #2b2b22;
    --ink-soft: #45453a;
    --map-tone: #b9c79a;
    --map-shade: #8f9d76;
    --band-tone: #c8b98c;
    --band-shade: #a8966a;
  }
  * { box-sizing: border-box; margin: 0; padding: 0; }
  html, body {
    width: 1200px;
    height: 750px;
    overflow: hidden;
    background: var(--backdrop);
    font-family: "Open Sans", Arial, sans-serif;
    color: var(--ink);
  }
  .label-sheet {
    display: flex;
    justify-content: center;
    align-items: center;
    gap: 120px;
    width: 1200px;
    height: 750px;
  }
  .label {
    position: relative;
    width: 360px;
    height: 630px;
    background: var(--label-bg);
    border: 1px solid var(--label-edge);
  }
  .continent-art {
    position: absolute;
    left: 95px;
    top: 75px;
    width: 170px;
    height: 210px;
    background: radial-gradient(circle at 45% 40%, var(--map-tone), var(--map-shade));
    border-radius: 46% 54% 40% 60% / 40% 42% 58% 60%;
  }
  .brand-name {
    position: absolute;
    top: 352px;
    width: 100%;
    text-align: center;
    font-size: 28px;
    font-weight: 600;
    letter-spacing: 2px;
    text-transform: uppercase;
    color: var(--ink);
  }
  .varietal {
    position: absolute;
    top: 396px;
    width: 100%;
    text-align: center;
    font-size: 16px;
    font-weight: 600;
    letter-spacing: 1px;
    text-transform: uppercase;
    color: var(--ink);
  }
  .pattern-band {
    position: absolute;
    left: 0;
    width: 100%;
    height: 34px;
    background: linear-gradient(90deg, var(--band-tone), var(--band-shade), var(--band-tone), var(--band-shade), var(--band-tone));
    opacity: 0.85;
  }
  .front-label .pattern-band { top: 455px; }
  .origin {
    position: absolute;
    top: 545px;
    width: 100%;
    text-align: center;
    font-size: 12px;
    color: var(--ink-soft);
    line-height: 1.4;
  }
  .grape-mark {
    position: absolute;
    left: 158px;
    top: 60px;
    width: 44px;
    height: 52px;
    background: radial-gradient(circle at 50% 40%, var(--map-shade), var(--ink-soft));
    border-radius: 50% 50% 50% 50% / 40% 40% 60% 60%;
  }
  .story {
    position: absolute;
    top: 200px;
    left: 30px;
    right: 30px;
    text-align: center;
    font-size: 11.4px;
    line-height: 1.55;
    color: var(--ink);
  }
  .back-label .pattern-band { top: 555px; }
</style>
</head>
<body>
<main class="label-sheet">
  <section class="label front-label">
    <div class="continent-art" role="img" aria-label="Map of Africa filled with a cluster of pale green grapes"></div>
    <h1 class="brand-name">Kavenzira</h1>
    <p class="varietal">Shiraz</p>
    <div class="pattern-band" role="img" aria-label="Band of African woven geometric pattern"></div>
    <p class="origin">South Africa<br>2005</p>
  </section>

  <section class="label back-label">
    <div class="grape-mark" role="img" aria-label="Small grape bunch emblem"></div>
    <p class="story">Kept quiet about where this wine began, we can only say it was chosen from the finest cellars on the continent. Kavenzira is a Shona word that speaks of honour, praise and being held in high regard. Brace yourself, because this Shiraz arrives as a storm of flavour. Deep, spiced and fruit-forward notes meet the palate with warmth and purpose, best enjoyed alongside sadza or nsima, roasted beef and dried greens simmered in peanut sauce. Carrying the glow, rhythm and spirit of an African braai, with bold flavours rising from every glass, Kavenzira turns each pour into a quiet gesture of respect and distinction. Open it slowly, share it generously, and let the conversation around the fire carry on long after the bottle is empty.</p>
    <div class="pattern-band" role="img" aria-label="Band of African woven geometric pattern"></div>
  </section>
</main>
</body>
</html>
```